Redesign This Psychology Website

We would like a slight redesign of this successful psychology (relationship counselling) website:

www.TheWillowNook.com.au

We are updating the website, and we'd like a slight refresh of the design and style.

Please keep to very similar colours, and use the same logo. We're looking for around 10 page templates, however the main one is the home page.

Keep in mind, this website already converts quite well, so we want a new, fresh design in keeping with this one. Please don't bother designing something too extremely different.

thanks :)

Target Market(s)

couples who are looking for relationship counselling. Men and women, 25 - 70, across Australia

Industry/Entity Type

Psychology

Number of Pages Required

5+ page

Font styles to use
Sans Serif

Colors
87cfc6
b7a5cd
ec1f27
ffffff
cee9f5

Requirements
Must have
• a similar look to the current design, just looking for a slight refresh.
• Search bar
• Areas for lots of photos
• same logo
• lots of content areas
Nice to have
• great content areas, where we can display a lot of content and our areas.
Should not have
• no colors like orange, etc.
• should not have a totally different feel.

```html
<!DOCTYPE html>
<html lang="en">
<head>
<meta charset="utf-8">
<title>The Willow Nook – Relationship &amp; Marriage Counselling</title>
<link href="https://fonts.googleapis.com/css2?family=Lato:wght@400;700;900&family=Open+Sans:wght@400;600;700&display=swap" rel="stylesheet">
<style>
:root{
  --teal:#18838f;
  --teal-dark:#0f6f7a;
  --aqua:#87cfc6;
  --aqua-soft:#d6efee;
  --frame:#bfe4e3;
  --red:#e3202b;
  --lilac:#b7a5cd;
  --sky:#cee9f5;
  --ink:#4a4a4a;
  --muted:#7d7d7d;
  --line:#dcdcdc;
  --white:#ffffff;
}
*{box-sizing:border-box;margin:0;padding:0}
html,body{width:1200px;height:4511px;overflow:hidden}
body{position:relative;background:var(--white);font-family:"Open Sans",Arial,sans-serif;color:var(--ink);font-size:13px;line-height:1.55}
.abs{position:absolute}
h1,h2,h3{font-family:"Lato",Arial,sans-serif;font-weight:400}
.red{color:var(--red)}
.teal{color:var(--teal)}
.btn{display:inline-block;background:var(--teal);color:var(--white);font-family:"Lato",sans-serif;font-weight:700;font-size:15px;letter-spacing:.5px;text-transform:uppercase;padding:13px 28px;border-radius:3px}
.read-more{font-family:"Lato",sans-serif;font-weight:900;font-size:17px;color:var(--teal);text-decoration:underline;letter-spacing:.5px}
.photo{position:absolute}

/* header */
.brand{left:75px;top:22px;display:flex;align-items:center;gap:12px}
.brand-dot{width:56px;height:56px;border-radius:50%;background:var(--teal)}
.brand-name{font-family:"Lato",sans-serif;font-weight:700;font-size:34px;color:var(--teal);line-height:1}
.brand-tag{font-size:12px;color:var(--teal);margin-top:4px}
.topbar{right:75px;top:18px;display:flex;align-items:center;gap:12px;font-size:11px;color:var(--teal);text-transform:uppercase}
.topbar .socials{display:flex;gap:6px}
.topbar .socials span{width:14px;height:14px;border-radius:50%;background:var(--red);display:block}
.topbar .sep{color:var(--line)}
.topbar .join{color:var(--red);font-weight:600}
.search{left:585px;top:62px;width:210px;height:34px;border:1px solid var(--line);border-radius:3px;display:flex;align-items:center;justify-content:space-between;padding:0 10px;color:#aaa;font-size:12px}
.help{left:815px;top:60px;display:flex;align-items:center;gap:10px;font-family:"Lato",sans-serif}
.help .lbl{color:var(--muted);font-size:17px}
.help .phone-badge{width:38px;height:38px;border-radius:50%;background:var(--teal);display:flex;align-items:center;justify-content:center}
.help .num{color:var(--teal);font-size:22px;font-weight:700}

/* frame */
.frame{left:78px;top:128px;width:1044px;height:4262px;border:4px solid var(--frame);border-radius:4px}
.nav{left:90px;top:132px;display:flex;gap:4px}
.nav a{display:block;padding:14px 15px;border:1px solid var(--frame);border-bottom:none;font-family:"Lato",sans-serif;font-size:14px;color:var(--teal);text-transform:uppercase;background:var(--white);border-radius:3px 3px 0 0}
.nav a.active{background:var(--teal);color:var(--white)}

/* hero */
.hero{left:90px;top:188px;width:1020px;height:470px;background:linear-gradient(90deg,#f6f1ea 0%,#efe6dc 40%,#d8c2ad 70%,#b8957a 100%)}
.hero-copy{left:125px;top:312px;width:560px}
.hero-copy h1{font-weight:900;font-size:40px;line-height:1.15;color:var(--teal)}
.hero-copy p{font-size:17px;margin:18px 0 28px;color:#333;line-height:1.35}

/* about */
.about{left:90px;top:706px;width:1020px;text-align:center}
.about h2{font-size:46px;line-height:1.1;color:var(--teal)}
.about p{width:730px;margin:8px auto 14px;font-size:13px;line-height:1.5}
.tiles{left:90px;top:918px;display:flex;gap:10px}
.tile{position:relative;width:247px;height:195px}
.tile .label{position:absolute;left:0;right:0;bottom:0;height:42px;background:rgba(135,207,198,.85);display:flex;align-items:center;padding:0 12px;font-family:"Lato",sans-serif;font-weight:700;font-size:16px;color:#1e3b3f;line-height:1.1}
.tile.quiz{background:#2d2826;color:var(--white);text-align:center;padding-top:14px}
.tile.quiz h3{font-weight:700;font-size:17px}
.tile.quiz .need{margin:10px 16px 6px;background:#4a4341;padding:3px;font-size:12px;font-weight:700}
.tile.quiz .list{font-size:11px;line-height:1.35;padding:0 18px}
.tile.quiz .label{background:var(--red);color:var(--white);justify-content:center}

/* psychologists */
.psych{left:105px;top:1232px;width:500px}
.psych h2{font-size:40px;line-height:1.12}
.psych p{margin-top:16px;font-size:13px}
.psych .btn{margin-top:22px}
.finder{left:625px;top:1255px;width:465px;height:380px;background:var(--white);border:6px solid #e8f1f2;box-shadow:0 6px 18px rgba(0,0,0,.25);padding:22px 30px;transform:rotate(1deg)}
.finder h2{font-size:36px;color:var(--teal);text-align:center;line-height:1.12}
.field{display:flex;align-items:center;justify-content:flex-end;gap:10px;margin-top:16px;font-size:15px;color:#555}
.field .box{width:180px;height:30px;border:1px solid var(--line);background:#f7f7f7;font-size:11px;padding:6px 8px;color:#888}
.or{text-align:right;padding-right:80px;margin-top:6px;color:#777}
.finder .btn{position:absolute;right:30px;bottom:22px;padding:10px 34px}

/* locations */
.locs{left:90px;top:1722px;width:1020px;text-align:center}
.locs h2{font-size:46px;color:var(--teal);line-height:1.1}
.locs p{margin:14px 0 16px;font-size:13px}
.loc-grid{left:100px;top:1868px;width:1000px;display:grid;grid-template-columns:245px 255px 230px 185px 160px;row-gap:12px;font-size:14px}
.loc-grid span{display:flex;align-items:center;gap:6px}
.loc-grid i{width:16px;height:16px;border-radius:50%;background:var(--aqua);display:block;flex:none}
.loc-grid b{font-weight:700}

/* feature rows */
.approach-bg{left:90px;top:2040px;width:1020px;height:370px;background:linear-gradient(90deg,#eef4f5,#f7fbfb)}
.feature h2{font-size:40px;line-height:1.15}
.feature p{font-size:13px;margin-top:12px}
.feature .read-more{display:block;text-align:right;margin-top:10px}

/* blogs */
.blogs-title{left:90px;top:3196px;width:1020px;text-align:center;font-size:42px;line-height:1.1;color:var(--teal)}
.blog-card .title{font-size:12px;color:var(--red);margin-top:8px}
.blog-card p{font-size:13px;margin-top:4px}
.blog-item{display:flex;gap:18px;align-items:flex-start}
.blog-item .thumb{width:78px;height:78px;flex:none}
.blog-item h3{font-size:18px;color:#333;line-height:1.25}
.blog-item .date{font-size:12px;color:var(--muted);margin-top:4px}

/* faq */
.faq-title{left:90px;top:3620px;width:1020px;text-align:center;font-size:42px;line-height:1.1;color:var(--teal)}
.faq{left:200px;top:3685px;width:800px}
.faq-item{border:1px solid var(--line);margin-bottom:12px}
.faq-q{display:flex;justify-content:space-between;align-items:center;padding:9px 14px;font-size:15px;color:var(--red)}
.faq-q::before{content:"»";margin-right:10px;color:var(--red)}
.faq-q .t{flex:1}
.faq-q .sign{color:#888;font-size:18px}
.faq-a{border-top:1px solid var(--line);padding:12px 30px 14px 72px;font-size:14px;color:#555}
.faq-a .read-more{display:block;text-align:right;font-size:13px;color:var(--red);font-weight:400;font-family:"Open Sans",sans-serif}

/* newsletter */
.news-bg{left:90px;top:3985px;width:1020px;height:395px;background:linear-gradient(90deg,#e8eef0 0%,#f3f6f7 50%,#ffffff 75%)}
.news-title{left:700px;top:4030px;font-size:42px;color:var(--teal)}
.news-box{left:610px;top:4130px;width:450px;height:160px;background:#f6f6f6;box-shadow:0 3px 10px rgba(0,0,0,.15);padding:24px 30px}
.news-box p{font-size:14px;color:#777;line-height:1.4;padding-right:20px}
.news-box .tab{position:absolute;right:18px;top:-8px;width:24px;height:40px;background:var(--teal)}
.email{margin-top:16px;display:flex;height:38px}
.email .in{flex:1;background:var(--white);border:1px solid var(--line);padding:9px 12px;font-size:12px;color:#aaa}
.email .go{width:44px;background:var(--red);display:flex;align-items:center;justify-content:center}

/* footer */
.foot-brand{left:78px;top:4398px;display:flex;align-items:center}
.foot-brand .brand-dot{width:62px;height:62px}
.foot-links{left:260px;top:4410px;width:680px;text-align:center;font-size:12px;color:#555}
.foot-links span{margin:0 10px}
.foot-copy{left:260px;top:4442px;width:680px;text-align:center;font-size:13px;color:#555}
.foot-copy b{color:var(--red)}
.foot-social{left:1000px;top:4418px;display:flex;gap:12px}
.foot-social span{width:36px;height:36px;border-radius:50%;background:var(--teal);display:block}
</style>
</head>
<body>

<header>
  <div class="abs brand">
    <span class="brand-dot"></span>
    <div>
      <div class="brand-name">The Willow Nook</div>
      <div class="brand-tag">helping you create loving relationships</div>
    </div>
  </div>
  <div class="abs topbar">
    <div class="socials"><span></span><span></span><span></span></div>
    <span class="sep">|</span>
    <span class="join">Join Our Association Program</span>
    <span class="sep">|</span>
    <span>Marriage Counselling</span>
    <span class="sep">|</span>
    <span>Relationship Counselling</span>
  </div>
  <div class="abs search">Search...
    <svg width="16" height="16" viewBox="0 0 16 16"><circle cx="6.5" cy="6.5" r="5" fill="none" stroke="#555" stroke-width="2"/><line x1="10.5" y1="10.5" x2="15" y2="15" stroke="#555" stroke-width="2"/></svg>
  </div>
  <div class="abs help">
    <span class="lbl">Get Help Now!</span>
    <span class="phone-badge"><svg width="20" height="20" viewBox="0 0 24 24"><path d="M6.6 10.8a15 15 0 0 0 6.6 6.6l2.2-2.2a1 1 0 0 1 1-.25 11.4 11.4 0 0 0 3.6.57 1 1 0 0 1 1 1V20a1 1 0 0 1-1 1A17 17 0 0 1 3 4a1 1 0 0 1 1-1h3.5a1 1 0 0 1 1 1c0 1.25.2 2.45.57 3.57a1 1 0 0 1-.25 1z" fill="#fff"/></svg></span>
    <span class="num">1300 555 014</span>
  </div>
</header>

<div class="abs frame"></div>

<nav class="abs nav">
  <a class="active">Home</a><a>About Us</a><a>Resources</a><a>Counselling</a><a>Location</a><a>Quizzes</a><a>FAQ</a><a>Blog</a><a>Store</a><a>Contact Us</a>
</nav>

<section>
  <div class="abs hero" role="img" aria-label="Smiling couple embracing outdoors in winter clothing"></div>
  <div class="abs hero-copy">
    <h1>We Specialise in Relationship &amp; Marriage Counselling</h1>
    <p>"At the end of our life, what matters most<br>is how well did we love"</p>
    <span class="btn">Contact Us Now</span>
  </div>
</section>

<section class="abs about">
  <h2>About Our <span class="teal">Willow Nook</span></h2>
  <p>At The Willow Nook, we are a group of PSYCHOLOGISTS, Australia wide who are passionate about relationships and helping you with yours. Our vision is to provide the most highly regarded and comprehensive marriage counselling and relationship counselling, and sex therapy in Australia, at reasonable and affordable rates.</p>
  <span class="btn">Read More</span>
</section>

<section class="abs tiles">
  <div class="tile" style="background:linear-gradient(180deg,#cfe3ec,#9fc6d3)" role="img" aria-label="Couple standing on a pier by the sea">
    <div class="label">Relationship Counselling</div>
  </div>
  <div class="tile quiz">
    <h3>Sex Therapy Counselling</h3>
    <div class="need">Do you need help with:</div>
    <div class="list">Low libido, erectile difficulties, premature ejaculation, differing desire, keeping sex exciting</div>
    <div class="label">Take our Sex Quiz</div>
  </div>
  <div class="tile" style="background:linear-gradient(180deg,#f2f2f2,#d6d6d6)" role="img" aria-label="Frustrated man sitting at a desk">
    <div class="label">Anger Management Counselling</div>
  </div>
  <div class="tile" style="background:linear-gradient(180deg,#c9d9e4,#8fa9b8)" role="img" aria-label="Woman looking at her reflection">
    <div class="label">Narcissism Counselling</div>
  </div>
</section>

<section class="abs psych">
  <h2><span class="teal">Our Willow Nook Relationship</span><br><span class="red">Psychologists</span></h2>
  <p>Our team of 75 hand chosen Registered Psychologists in 81 locations Australia wide, are individually selected for their knowledge, experience, compassion, and unbiased approach to marriage counselling and sexual therapy.</p>
  <p>In addition all our Psychologists take part in our initial Relationship Counselling Methodologies Training and yearly in-house conferences, ensuring you are in safe and experienced hands.</p>
  <p>As we are Psychologists, you may be eligible for Government &amp; Private Health Insurance Rebates.</p>
  <span class="btn">Read More</span>
</section>

<section class="abs finder">
  <h2>Find Our Psychologist<br>Near You</h2>
  <div class="field">Type of Counselling : <span class="box">Select...</span></div>
  <div class="field">Location : <span class="box"></span></div>
  <div class="or">OR</div>
  <div class="field" style="margin-top:6px">Postal Code : <span class="box"></span></div>
  <span class="btn">Search</span>
</section>

<section class="abs locs">
  <h2>Our Relationship Counselling Locations<br><span class="red">across Australia</span></h2>
  <p>We currently have relationship counselling and marriage counselling services in:</p>
</section>
<div class="abs loc-grid">
  <span><i style="background:var(--red)"></i><b>Sydney</b> – 19 centres</span>
  <span><i></i><b>Brisbane</b> – 14 centres</span>
  <span><i></i><b>Adelaide</b> – 4 centres</span>
  <span><i></i><b>Cairns</b> – 1 centre</span>
  <span></span>
  <span><i></i><b>Canberra</b> – 2 centres</span>
  <span><i></i><b>Wollongong</b> – 1 centre</span>
  <span><i></i><b>Gold Coast</b> – 5 centres</span>
  <span><i></i><b>Townsville</b> – 1 centre</span>
  <span></span>
  <span><i></i><b>Melbourne</b> – 21 centres</span>
  <span><i></i><b>Central Coast</b> – 2 centres</span>
  <span><i></i><b>Sunshine Coast</b> – 2 centres</span>
  <span><i></i><b>Wodonga</b> – 1 centre</span>
  <span></span>
  <span><i></i><b>Perth</b> – 11 centres</span>
</div>

<section>
  <div class="abs approach-bg"></div>
  <div class="photo" style="left:90px;top:2040px;width:470px;height:370px;background:linear-gradient(135deg,#c7dce8,#e8d8cc)" role="img" aria-label="Mature couple smiling together"></div>
  <div class="abs feature" style="left:595px;top:2085px;width:480px">
    <h2><span class="teal">Our Relationship</span><br><span class="red">Counselling Approach</span></h2>
    <p>It is an important part of our policy to take a very positive approach to our relationship counselling.</p>
    <p>We feel it is important to really understand the problems and perspectives of each of you, and at the same time, we find that most couples are looking to find a positive action plan and way through their problems to make changes...</p>
    <span class="read-more">READ MORE</span>
  </div>
</section>

<section>
  <div class="photo" style="left:795px;top:2425px;width:315px;height:340px;background:radial-gradient(circle at 55% 50%,#d9c6b6,#f3ede8 60%,#fff 80%)" role="img" aria-label="Playful couple laughing together"></div>
  <div class="abs feature" style="left:95px;top:2460px;width:700px">
    <h2><span class="teal">Communication is a vital skill but</span><br><span class="red">not often taught to us.</span></h2>
    <div style="width:600px">
      <p>Most people find that their ways of communicating with each other are what hamper us from having a happy healthy relationship.</p>
      <p>Effective Interpersonal Communication skills are not something that we are usually taught. But for almost everyone who is having difficulties in their relationship, they feel that they are trying to communicate their thoughts and feelings but that their partner is not listening...</p>
      <span class="read-more">READ MORE</span>
    </div>
  </div>
</section>

<section>
  <div class="photo" style="left:90px;top:2800px;width:1020px;height:360px;background:linear-gradient(90deg,#cfe2ea 0%,#eef5f7 35%,#f9fbfc 60%,#fff 100%)" role="img" aria-label="Smiling woman with short blonde hair"></div>
  <div class="abs feature" style="left:460px;top:2822px;width:600px">
    <h2 style="font-size:38px"><span class="teal">We as individuals have </span><span class="red">specific patterns in our relationships</span></h2>
    <p>We can also assist you if you want individual help and guidance on your relationship, so you can learn what the patterns in your relationships are showing you about yourself.</p>
    <p>If you have been in a number of relationships and have found yourself repeating the same kind of experiences, which is often the way our relationships play out, we can help you discover the patterns that you might be unwittingly setting up, so you can change these and move into more rewarding relationships in the future...</p>
    <span class="read-more">READ MORE</span>
  </div>
</section>

<section class="blogs">
  <h2 class="abs blogs-title">Latest <span class="red">Blogs</span></h2>
  <div class="abs blog-card" style="left:145px;top:3275px;width:410px">
    <div style="height:175px;border:3px solid #dde9ef;background:linear-gradient(90deg,#dfe9ee,#f2ede6)" role="img" aria-label="Couple lying on the floor smiling"></div>
    <div class="title">Do You wonder Why You and Your Partner Are Together?!</div>
    <div style="font-size:12px;color:var(--red)">19 Oct, 2016</div>
    <p>Lorem ipsum dolor sit amet, consectetur adipiscing elit, sed do eiusmod tempor incididunt ut labore et dolore magna aliqua.</p>
  </div>
  <div class="abs" style="left:635px;top:3280px;width:400px;display:flex;flex-direction:column;gap:16px">
    <div class="blog-item"><div class="thumb" style="background:linear-gradient(135deg,#b8c6cf,#6f8391)" role="img" aria-label="Man looking thoughtful"></div><div><h3>Doubtful about Relationship Counselling</h3><div class="date">20 Feb, 2016</div></div></div>
    <div class="blog-item"><div class="thumb" style="background:linear-gradient(135deg,#c5b9ae,#857465)" role="img" aria-label="Couple sitting apart"></div><div><h3>Did your relationship Start on Rocky Ground?</h3><div class="date">20 Feb, 2016</div></div></div>
    <div class="blog-item"><div class="thumb" style="background:linear-gradient(135deg,#d6c3a8,#8f6f4b)" role="img" aria-label="Couple talking"></div><div><h3>What are you like in a relationship?</h3><div class="date">20 Feb, 2016</div></div></div>
  </div>
</section>

<h2 class="abs faq-title">FAQ's</h2>
<section class="abs faq">
  <div class="faq-item">
    <div class="faq-q"><span class="t">What are the fees involved, and are there any rebates?</span><span class="sign">–</span></div>
    <div class="faq-a">Private health rebates should apply if you have 'psychology' as an extra, but we recommend that you call your fund and check your level of cover if this is of concern to you. Unfortunately funds don't give us these details.<span class="read-more">READ MORE</span></div>
  </div>
  <div class="faq-item"><div class="faq-q"><span class="t">What happens in a marriage/relationship counselling session?</span><span class="sign">+</span></div></div>
  <div class="faq-item"><div class="faq-q"><span class="t">How helpful will it be?</span><span class="sign">+</span></div></div>
</section>

<section>
  <div class="abs news-bg"></div>
  <div class="photo" style="left:90px;top:3985px;width:520px;height:395px;background:radial-gradient(ellipse at 40% 55%,#d8c9bc,#eef2f4 65%,rgba(255,255,255,0) 90%)" role="img" aria-label="Couple smiling at the beach"></div>
  <h2 class="abs news-title">Sucribe Newsletter</h2>
  <div class="abs news-box">
    <span class="abs tab"></span>
    <p>Sign up for our weekly newsletter to receive updates, news, and promos.</p>
    <div class="email"><span class="in">Email</span><span class="go"><svg width="18" height="18" viewBox="0 0 24 24"><path d="M2 21 23 12 2 3v7l15 2-15 2z" fill="#fff"/></svg></span></div>
  </div>
</section>

<footer>
  <div class="abs foot-brand"><span class="brand-dot"></span></div>
  <div class="abs foot-links"><span>Privacy Policy</span>|<span>Terms &amp; Conditions</span>|<span>Site Map</span>|<span>Associate Psychologists Program</span>|<span>Contact Us</span></div>
  <div class="abs foot-copy">© <b>The Willow Nook</b> - 2017. All Rights Reserved.</div>
  <div class="abs foot-social"><span></span><span></span><span></span></div>
</footer>

</body>
</html>
```